Flyer für IT-Firma
Zielgruppe
Wir sind eine IT-Firma, die sich unter anderem auf IT-Netzwerke spezialisiert hat. Wir verkaufen Netzwerklösungen, aber auch Produkte im Bereich IT Netzwerk, IT Security, WLAN, Cloud-Lösungen, etc. und Services. Unsere Zielgruppen für diesen Bereich sind kleinere bis Mittlere Unternehmen aber auch öffentliche Verwaltungen, Schulen, Spitäler etc. die ihre IT Netzwerke verbessern möchten und sich absichern möchten für den Fall von WLAN Ausfall oder Datenverlust. Diese Zielgruppen kennen uns womöglich noch nicht oder haben in einem anderen Projekt mit uns zusammengearbeitet. Der Flyer soll sie also von uns und dem Produkt überzeugen.
Aufgabenstellung
Der Flyer soll 2-Seitig oder 4-Seitig sein. Er soll als Vorlage für die Präsentation verschiedenster Produkte dienen. Ziel ist es einen Flyer zu haben im einheitlichen Design, den wir beliebig mit Fotos und Text abfüllen können. So dass wir unsere Produkte und Dienstleistungen im einheitlichen Design vorstellen können. Der Flyer soll folgende Elemente beinhalten:
Seite 1 eher oberflächlich das Produkt vorstellen
- Logo
- Einleitung zum Unternehmen und oder Produkt
- 1-2 Platzhalter für Bilder
- Weiterer Text für Produktbeschreibung
Seite 2 detaillierte Informationen:
- technische Daten (allenfalls in Listenform)
- Weitere Detailinformationen
- Preise
- Kontakt
Vorzugsweise Format A4 damit man auch daraus einfach ein PDF generieren kann und per Mail versenden kann. Vorschläge für andere Formate sind willkommen.

```html
<!DOCTYPE html>
<html lang="de">
<head>
<meta charset="utf-8">
<title>NVX Solutions – Produktflyer</title>
<link href="https://fonts.googleapis.com/css2?family=Lato:ital,wght@0,300;0,400;0,700;0,900;1,400;1,700;1,900&display=swap" rel="stylesheet">
<style>
  :root{
    --bg:#e9eaea;
    --paper:#f8f8f7;
    --teal:#3f7b87;
    --teal-dark:#264f5c;
    --green:#7ab648;
    --orange:#eba033;
    --mint:#e2eeed;
    --ink:#333b40;
    --grey:#6f767a;
  }
  *{box-sizing:border-box;margin:0;padding:0}
  html,body{width:1200px;height:800px;overflow:hidden}
  body{background:var(--bg);font-family:'Lato',sans-serif;color:var(--ink);position:relative}
  .page{position:absolute;top:40px;width:510px;height:720px;background:var(--paper);overflow:hidden;box-shadow:0 18px 40px rgba(0,0,0,.12)}
  .page--front{left:60px}
  .page--back{left:630px}

  /* brand */
  .brand{display:flex;align-items:center;gap:8px}
  .brand__mark{width:14px;height:14px;background:var(--teal)}
  .brand__name{font-weight:400;color:var(--ink);line-height:1}
  .brand__sub{display:block;font-size:.42em;color:var(--ink);margin-top:2px;letter-spacing:.5px}

  /* front */
  .hero{position:absolute;left:0;top:0;width:100%;height:300px;background:radial-gradient(circle at 68% 35%,#5fc4d8 0,#2a7890 18%,#1d4a5e 45%,#142d3b 80%)}
  .logo-tab{position:absolute;left:0;top:22px;width:250px;height:64px;background:#fff;border-radius:0 14px 14px 0;padding:12px 0 0 22px}
  .logo-tab .brand__name{font-size:28px}
  .banner-accent{position:absolute;right:0;top:255px;width:80px;height:62px;background:var(--green);border-radius:0 0 0 14px}
  .banner{position:absolute;left:38px;right:28px;top:262px;height:70px;background:var(--teal);border-radius:30px 14px 14px 0;padding:12px 0 0 22px;color:#fff}
  .banner__title{font-weight:900;font-size:24px;letter-spacing:.3px;line-height:1}
  .banner__sub{font-size:14px;font-weight:400;margin-top:6px}
  .banner-curve{position:absolute;left:38px;top:330px;width:30px;height:30px;border-left:4px solid var(--teal);border-radius:0 0 0 30px}
  .intro{position:absolute;left:60px;right:28px;top:352px}
  .intro__title{color:var(--teal);font-style:italic;font-weight:900;font-size:14px;line-height:1.25}
  .intro__text{font-size:8.2px;line-height:1.5;margin-top:8px;color:var(--ink)}
  .product-zone{position:absolute;left:24px;right:0;top:468px;bottom:0;background:var(--mint);border-radius:28px 0 0 0}
  .photo{position:absolute;border:5px solid #fff;border-radius:12px;box-shadow:0 6px 14px rgba(0,0,0,.18)}
  .photo--one{left:18px;top:14px;width:150px;height:110px;background:radial-gradient(circle at 55% 45%,#9fe0f2 0,#3a8fb4 25%,#173a55 70%)}
  .photo--two{left:60px;top:110px;width:155px;height:110px;background:radial-gradient(circle at 50% 60%,#f4c16a 0,#7a6a4a 30%,#2f3b3a 75%)}
  .product{position:absolute;left:230px;right:20px;top:16px}
  .product__title{color:var(--teal);font-style:italic;font-weight:900;font-size:12px}
  .product__text{font-size:8px;line-height:1.5;margin-top:4px}
  .product__list{list-style:none;margin-top:6px}
  .product__list li{font-size:8px;line-height:1.5;padding-left:12px;position:relative;margin-bottom:4px}
  .product__list li::before{content:"";position:absolute;left:0;top:4px;width:5px;height:5px;border-radius:50%;background:var(--green)}
  .footer-band{position:absolute;left:0;right:0;bottom:0;height:36px;background:var(--orange);border-radius:0 22px 0 0;display:flex;align-items:center;justify-content:space-between;padding:0 22px;color:#fff;font-size:10px;font-weight:700}

  /* back */
  .tab{position:absolute;left:28px;top:30px;width:290px;height:40px;background:var(--teal);border-radius:16px 6px 6px 0;color:#fff;font-weight:900;font-style:italic;font-size:18px;padding:9px 0 0 28px}
  .tab-curve{position:absolute;left:28px;top:68px;width:18px;height:18px;border-left:3px solid var(--teal);border-radius:0 0 0 18px}
  .label{color:var(--teal);font-weight:900;font-style:italic;font-size:10px}
  .body-it{font-style:italic;font-size:8px;line-height:1.55}
  .desc{position:absolute;left:48px;right:30px;top:84px}
  .desc .body-it{margin-top:5px}
  .spec{position:absolute;left:40px;top:170px;width:175px}
  .spec table{border-collapse:collapse;margin-top:6px;width:100%}
  .spec th{color:var(--green);font-weight:400;font-style:italic;font-size:7.5px;text-align:left;padding-bottom:5px}
  .spec td{font-style:italic;font-size:8px;padding:2px 0}
  .features{position:absolute;left:250px;right:28px;top:190px}
  .checks{list-style:none;margin-top:6px}
  .checks li{position:relative;padding-left:14px;font-style:italic;font-size:8px;line-height:1.5;margin-bottom:5px}
  .checks svg{position:absolute;left:0;top:2px;width:9px;height:7px}
  .checks b{font-weight:700}
  .benefits{position:absolute;left:34px;top:365px;width:185px}
  .prices{position:absolute;left:248px;right:28px;top:405px;text-align:center}
  .prices .body-it{margin-top:4px}
  .tiers{display:flex;justify-content:space-between;margin-top:12px}
  .tier{width:46%}
  .tier__badge{display:inline-block;color:#fff;font-weight:900;font-size:8px;padding:3px 14px;border-radius:5px}
  .tier__badge--basic{background:var(--green)}
  .tier__badge--ent{background:var(--orange)}
  .tier__price{font-weight:900;font-size:24px;margin-top:6px}
  .tier__price small{font-size:12px;vertical-align:top}
  .tier__price--basic{color:var(--green)}
  .tier__price--ent{color:var(--orange)}
  .tier .body-it{color:var(--grey);text-align:center}
  .contact{position:absolute;left:0;right:0;top:572px;bottom:0;background:var(--mint);border-radius:0 28px 0 0}
  .contact .brand{position:absolute;left:26px;top:18px}
  .contact .brand__name{font-size:20px}
  .partner-badge{position:absolute;left:28px;top:62px;width:62px;height:24px;border-radius:4px;background:#c9dcde}
  .office{position:absolute;top:22px;font-size:7.5px;line-height:1.55;color:var(--grey)}
  .office h4{color:var(--green);font-size:7.5px;font-weight:900;margin-bottom:3px}
  .office--main{left:220px}
  .office--branch{left:360px}
</style>
</head>
<body>

<section class="page page--front">
  <div class="hero" role="img" aria-label="Foto: Hände an einem Tablet mit leuchtenden Netzwerk-Symbolen"></div>
  <div class="logo-tab">
    <div class="brand"><span class="brand__mark"></span><span class="brand__name">nvx solutions<span class="brand__sub">by netravon</span></span></div>
  </div>
  <div class="banner-accent"></div>
  <div class="banner">
    <div class="banner__title">VERBUNDEN MIT DER ZUKUNFT</div>
    <div class="banner__sub">Die Experten für Kommunikationstechnologien</div>
  </div>
  <div class="banner-curve"></div>

  <div class="intro">
    <h2 class="intro__title">NVX Network Solutions – Ihr Partner<br>für sichere und effiziente Netzwerklösungen</h2>
    <p class="intro__text">Netravon ist ein Schweizer Unternehmen, das sich auf massgeschneiderte Netzwerklösungen für Geschäftskunden spezialisiert hat. Mit über 30 Jahren Erfahrung und starken Partnern entwickeln wir zukunftsorientierte IT-Infrastrukturen. Unsere Experten begleiten Sie von der Planung bis zur Umsetzung und bieten 24-Stunden-Support für reibungslose Abläufe. Vertrauen Sie auf unsere Kompetenz in Netzwerken, Security, WLAN und Cloud.</p>
  </div>

  <div class="product-zone">
    <div class="photo photo--one" role="img" aria-label="Foto: Hände mit leuchtender Weltkugel"></div>
    <div class="photo photo--two" role="img" aria-label="Foto: Hand mit leuchtenden Technologie-Symbolen"></div>
    <div class="product">
      <h3 class="product__title">Ihr Produkte Name</h3>
      <p class="product__text">Lorem ipsum dolor sit amet, consectetuer adipiscing elit, sed diam nonummy nibh euismod tincidunt.</p>
      <ul class="product__list">
        <li>Lorem ipsum dolor sit amet, sed diam nonummy nibh euismod tincidunt ut laoreet dolore magna aliquam erat volutpat.</li>
        <li>Ut wisi enim ad minim veniam, quis nostrud exerci tation ullam corper suscipit lobortis nisl ut aliquip ex ea commodo consequat.</li>
        <li>Duis autem vel eum iriure dolor in hendrerit in vulputate velit esse molestie consequat, vel illum dolore eu feugiat nulla facilisis.</li>
      </ul>
    </div>
  </div>

  <footer class="footer-band"><span>nvx solutions by netravon | Your Slogan goes here</span><span>www.netravon.ch</span></footer>
</section>

<section class="page page--back">
  <div class="tab">PRODUCT TECHNICAL DATA</div>
  <div class="tab-curve"></div>

  <div class="desc">
    <h3 class="label">Production Description</h3>
    <p class="body-it">Lorem ipsum dolor sit amet, consectetuer adipiscing elit, sed diam nonummy nibh euismod tincidunt ut laoreet dolore magna aliquam erat volutpat. Ut wisi enim ad minim veniam, quis nostrud exerci tation ullamcorper suscipit lobortis nisl ut aliquip ex ea commodo consequat. Duis autem vel eum iriure dolor in hendrerit.</p>
  </div>

  <div class="spec">
    <h3 class="label">Product Specification</h3>
    <table>
      <tr><th>Format</th><th>Size</th><th>Metric</th><th>Xx</th></tr>
      <tr><td>Lorem ipsum</td><td>12</td><td>cm</td><td>-</td></tr>
      <tr><td>Lorem ipsum</td><td>256</td><td>mm</td><td>-</td></tr>
      <tr><td>Lorem ipsum</td><td>7128</td><td>mm</td><td>-</td></tr>
      <tr><td>Lorem ipsum</td><td>092</td><td>cm</td><td>-</td></tr>
      <tr><td>Lorem ipsum</td><td>67</td><td>mm</td><td>-</td></tr>
      <tr><td>Lorem ipsum</td><td>89</td><td>mm</td><td>-</td></tr>
      <tr><td>Lorem ipsum</td><td>90</td><td>mm</td><td>-</td></tr>
      <tr><td>Lorem ipsum</td><td>309</td><td>mm</td><td>-</td></tr>
      <tr><td>Lorem ipsum</td><td>596</td><td>mm</td><td>-</td></tr>
    </table>
  </div>

  <div class="features">
    <h3 class="label">Key Features</h3>
    <ul class="checks">
      <li><svg viewBox="0 0 9 7"><path d="M1 3.5 3.5 6 8 1" fill="none" stroke="#7ab648" stroke-width="1.6"/></svg>Lorem ipsum dolor sit amet, consectetuer adipiscing elit, sed diam nonummy nibh euismod tincidunt.</li>
      <li><svg viewBox="0 0 9 7"><path d="M1 3.5 3.5 6 8 1" fill="none" stroke="#7ab648" stroke-width="1.6"/></svg>Lorem ipsum dolor sit amet, consectetuer adipiscing elit, sed diam nonummy nibh euismod tincidunt.</li>
      <li><svg viewBox="0 0 9 7"><path d="M1 3.5 3.5 6 8 1" fill="none" stroke="#7ab648" stroke-width="1.6"/></svg>Lorem ipsum dolor sit amet, consectetuer</li>
      <li><svg viewBox="0 0 9 7"><path d="M1 3.5 3.5 6 8 1" fill="none" stroke="#7ab648" stroke-width="1.6"/></svg>Lorem ipsum dolor sit amet, consectetuer adipiscing elit, sed diam nonummy nibh euismod tincidunt.</li>
      <li><svg viewBox="0 0 9 7"><path d="M1 3.5 3.5 6 8 1" fill="none" stroke="#7ab648" stroke-width="1.6"/></svg>Lorem ipsum dolor sit amet, consectetuer adipiscing elit, sed diam nonummy nibh euismod tincidunt.</li>
    </ul>
  </div>

  <div class="benefits">
    <h3 class="label">Key Benefits</h3>
    <ul class="checks">
      <li><svg viewBox="0 0 9 7"><path d="M1 3.5 3.5 6 8 1" fill="none" stroke="#7ab648" stroke-width="1.6"/></svg><b>Lorem ipsum dolor sit amet,</b> consectetuer adipiscing elit, sed diam nonummy nibh euismod tincidunt.</li>
      <li><svg viewBox="0 0 9 7"><path d="M1 3.5 3.5 6 8 1" fill="none" stroke="#7ab648" stroke-width="1.6"/></svg><b>Lorem ipsum dolor sit amet,</b> consectetuer adipiscing elit, sed diam nonummy nibh euismod tincidunt.</li>
      <li><svg viewBox="0 0 9 7"><path d="M1 3.5 3.5 6 8 1" fill="none" stroke="#7ab648" stroke-width="1.6"/></svg><b>Lorem ipsum dolor sit amet,</b> consectetuer adipiscing elit, sed diam nonummy nibh euismod tincidunt.</li>
    </ul>
  </div>

  <div class="prices">
    <h3 class="label">Product Prices</h3>
    <p class="body-it">Lorem ipsum dolor sit amet, consectetuer adipiscing elit, sed diam nonummy nibh euismod tincidunt.</p>
    <div class="tiers">
      <div class="tier">
        <span class="tier__badge tier__badge--basic">BASIC</span>
        <div class="tier__price tier__price--basic"><small>€</small>100</div>
        <p class="body-it">Lorem ipsum dolor sit amet, consectetuer adipiscing elit</p>
      </div>
      <div class="tier">
        <span class="tier__badge tier__badge--ent">ENTERPREISE</span>
        <div class="tier__price tier__price--ent"><small>€</small>2500</div>
        <p class="body-it">Lorem ipsum dolor sit amet, consectetuer adipiscing elit</p>
      </div>
    </div>
  </div>

  <div class="contact">
    <div class="brand"><span class="brand__mark"></span><span class="brand__name">nvx solutions<span class="brand__sub">by netravon</span></span></div>
    <div class="partner-badge"></div>
    <div class="office office--main">
      <h4>HAUPTSITZ</h4>
      Netravon AG<br>Lindenweg 14 |<br>6300 Zug<br>Telefon +41 41 555 20 10<br>Telefax +41 41 555 20 19<br>kontakt@netravon.ch
    </div>
    <div class="office office--branch">
      <h4>NIEDERLASSUNG</h4>
      Netravon AG<br>"Espace Riviera" Chemin du Lac 8 |<br>1110 Morges<br>Telefon +41 41 555 20 10<br>Telefax +41 41 555 20 19<br>kontakt@netravon.ch
    </div>
    <footer class="footer-band"><span>nvx solutions by netravon | Your Slogan goes here</span><span>www.netravon.ch</span></footer>
  </div>
</section>

</body>
</html>
```